WERBE-FLYER
Zielgruppe
Immobilien Makler
Aufgabenstellung
Überarbeitung des bestehenden Entwurfs.
Der Flyer wird an Hauseigentümer mit der Post verteilt (nicht adressierte Werbung).
Format:
offen A4 Querformat
geschlossen (1x gefaltet) A5 (4 Seiten)
In der Mitte eine Perforationslinie zum Abtrennen. Danach kann die Seite 3 & 4 zusammengefaltet (geklebt) werden und an uns zurückgeschickt werden.
Rücksendung erfolgt via Geschäftsantwortsendung - ohne Strichcode (siehe Vorlage Alpin. Kurier).

```html
<!DOCTYPE html>
<html lang="de">
<head>
<meta charset="utf-8">
<title>Norvala Immobilien – Flyer A4 quer, 1x gefaltet</title>
<link href="https://fonts.googleapis.com/css2?family=Abel&family=Arimo:wght@400;700&family=Bebas+Neue&family=Open+Sans:wght@400;600&display=swap" rel="stylesheet">
<style>
:root{
  --navy:#0d3558;
  --cyan:#27a9d6;
  --ink:#3b3b3b;
  --grey-text:#666a72;
  --panel:#efefef;
  --band:#a4a6ba;
  --caption:#8a8a8a;
  --paper:#ffffff;
}
*{box-sizing:border-box;margin:0;padding:0}
html,body{width:1190px;height:1200px;overflow:hidden;background:var(--paper)}
body{position:relative;font-family:"Open Sans",sans-serif;color:var(--ink)}
.spread{position:absolute;left:215px;width:760px;height:537px;background:var(--paper);border:1px solid #c9c9c9;overflow:hidden}
.spread--outside{top:22px}
.spread--inside{top:612px}
.abs{position:absolute}
.headline{font-family:"Bebas Neue",sans-serif;color:var(--navy);line-height:.92;letter-spacing:.2px}
.slash{color:var(--cyan)}
.captions{position:absolute;left:215px;width:760px;display:flex;justify-content:space-around;font-family:"Abel",sans-serif;font-size:30px;color:var(--caption)}
.captions--outside{top:565px}
.captions--inside{top:1155px}

/* Geschäftsantwort block */
.reply-mark{left:190px;top:4px;width:200px;height:100px}
.reply-letter{left:228px;top:12px;font-family:"Arimo",sans-serif;font-weight:700;font-size:38px;color:#333}
.reply-notice{left:295px;top:18px;font-family:"Arimo",sans-serif;font-size:6.5px;line-height:1.35;color:#333}
.reply-type{left:205px;top:65px;width:195px;text-align:center;font-family:"Arimo",sans-serif;font-weight:700;font-size:6.2px;line-height:1.5;color:#333}
.reply-address{left:190px;top:150px;font-family:"Arimo",sans-serif;font-weight:700;font-size:9.5px;line-height:1.55;color:#333}

/* Back panel */
.promo-top{left:0;top:318px;width:278px;height:7px;background:var(--navy)}
.promo-bottom{left:0;top:503px;width:278px;height:7px;background:var(--navy)}
.promo-side{left:271px;top:428px;width:7px;height:82px;background:var(--navy)}
.promo-title{left:24px;top:352px;font-size:30px}
.promo-text{left:24px;top:435px;font-size:10px;line-height:1.35;color:var(--navy)}

/* Cover */
.cover-photo{left:464px;top:33px;width:283px;height:471px;background:linear-gradient(180deg,#7f90a8 0%,#b9c4d2 22%,#e6e8ea 38%,#cfc8bd 58%,#a89a87 74%,#5b5a52 88%,#3e3f3a 100%)}
.cover-frame{left:400px;top:110px;width:270px;height:318px;border:8px solid var(--navy);border-right-width:8px}
.cover-title{left:428px;top:196px;font-size:52px;line-height:.93}
.cover-url{left:487px;top:412px;font-family:"Bebas Neue",sans-serif;font-size:15px;color:#fff;letter-spacing:.3px}
.brand{display:flex;align-items:center;gap:6px;font-family:"Open Sans",sans-serif;font-weight:600;color:var(--navy)}
.brand-square{display:block;background:var(--navy)}
.cover-brand{left:600px;top:60px;font-size:22px;letter-spacing:1px}
.cover-brand .brand-square{width:18px;height:18px}

/* Inside left */
.services-title{left:106px;top:40px;font-size:27px}
.side-label{left:22px;font-family:"Bebas Neue",sans-serif;font-size:11px;line-height:1.02;color:var(--navy)}
.body-copy{left:106px;width:245px;font-size:7px;line-height:1.5;color:var(--ink)}
.body-copy ul{padding-left:16px;margin-top:6px}
.body-copy p+p{margin-top:7px}
.contact-band{left:0;top:419px;width:380px;height:118px;background:var(--panel)}
.contact-box{left:95px;top:419px;width:257px;height:118px;background:var(--navy);color:#fff;font-size:7px;line-height:1.5;padding:10px 11px}
.contact-name{font-family:"Bebas Neue",sans-serif;font-size:16px;color:var(--cyan);line-height:1;margin-bottom:10px}
.contact-cols{display:flex;gap:28px;margin-top:10px}
.inside-brand{left:22px;top:442px;font-size:11px;letter-spacing:.5px}
.inside-brand .brand-square{width:10px;height:10px}

/* Perforation */
.perforation{left:380px;top:0;width:2px;height:537px;border-left:2px dashed var(--navy)}
.scissors{left:372px;top:455px;width:18px;height:22px}

/* Inside right */
.reply-panel{left:382px;top:0;width:378px;height:537px;background:var(--panel)}
.tape{left:382px;width:378px;height:18px;background:var(--band);color:#fff;font-size:5px;letter-spacing:.4px;text-align:center;line-height:18px}
.tape--top{top:0}
.tape--bottom{top:519px}
.values-frame{left:427px;top:42px;width:320px;height:210px;border:7px solid var(--navy);border-left:none}
.values-frame-left{left:427px;top:180px;width:7px;height:72px;background:var(--navy)}
.values-frame-topleft{left:427px;top:42px;width:7px;height:12px;background:var(--navy)}
.values-title{left:427px;top:60px;font-size:29px}
.values-copy{left:427px;top:108px;width:310px;font-size:6.8px;line-height:1.5}
.quote-mark{left:452px;top:188px;font-family:"Bebas Neue",sans-serif;font-size:44px;color:var(--cyan);line-height:1}
.quote-text{left:482px;top:190px;font-family:"Bebas Neue",sans-serif;font-size:16px;line-height:1.05;color:#7a7d84}
.fold-line{left:398px;top:264px;width:348px;border-top:1px solid #c4c4c4}
.fold-note{left:398px;top:255px;width:348px;text-align:center;font-size:5px;color:#999}
.reply-title{left:427px;top:287px;font-size:27px}
.reply-intro{left:427px;top:324px;font-size:7px}
.checklist{left:427px;top:343px;list-style:none;font-size:7px;color:var(--navy)}
.checklist li{display:flex;align-items:center;gap:6px;height:19px}
.checklist li::before{content:"";width:9px;height:9px;border:1px solid #777;background:#fff}
.field{position:absolute;width:128px;border-top:1px solid #777;padding-top:3px;font-size:7px;color:var(--navy)}
</style>
</head>
<body>

<!-- Aussen: Rückseite + Titelseite -->
<section class="spread spread--outside">
  <svg class="abs reply-mark" viewBox="0 0 200 100" aria-hidden="true">
    <line x1="8" y1="2" x2="8" y2="92" stroke="#444" stroke-width="9" stroke-dasharray="4 4"/>
    <line x1="22" y1="92" x2="198" y2="92" stroke="#444" stroke-width="9" stroke-dasharray="5 4"/>
  </svg>
  <div class="abs reply-letter">A</div>
  <div class="abs reply-notice">Nicht frankieren<br>Ne pas affranchir<br>Non affrancare</div>
  <div class="abs reply-type">Geschäftsantwortsendung Invio commerciale risposta<br>Envoi commercial-réponse</div>
  <div class="abs reply-address">NORVALA IMMOBILIEN AG<br>Lindenweg 12<br>8003 Zürich</div>

  <div class="abs promo-top"></div>
  <h2 class="abs headline promo-title">Wir suchen Bauland<br>für unsere Kunden!</h2>
  <p class="abs promo-text">Bei erfolgreicher Vermittlung erhalten Sie 1<br>Wochenende für 2 Personen im 4****Hotel<br>Riva Serena Locarno</p>
  <div class="abs promo-side"></div>
  <div class="abs promo-bottom"></div>

  <div class="abs cover-photo" role="img" aria-label="Foto: moderner weisser Hauseingang mit Holzsteg, Kies und Palmlilien in der Abenddämmerung"></div>
  <div class="abs cover-frame"></div>
  <h1 class="abs headline cover-title">Immobilien<br>sind unsere<br>Passion</h1>
  <div class="abs cover-url">NORVALA-IMMO.CH</div>
  <div class="abs brand cover-brand"><span class="brand-square"></span>NORVALA</div>
</section>
<div class="captions captions--outside"><span>Außen - Back</span><span>Außen - Cover</span></div>

<!-- Innen: links + Antwortkarte -->
<section class="spread spread--inside">
  <div class="abs reply-panel"></div>

  <h2 class="abs headline services-title">Unsere Dienstleistungen <span class="slash">/</span></h2>
  <div class="abs side-label" style="top:83px">Verkauf mit<br>Passion &amp;<br>Sachverstand</div>
  <div class="abs body-copy" style="top:80px">
    <p>Der Verkauf einer Immobilie ist ein vielschichtiger Prozess. Lieb gewonnene Liegenschaften, die über viele Jahre ein Zuhause waren, haben für die Verkäufer nicht nur einen Geldwert, sondern auch einen emotionalen Wert.</p>
    <p>Wir begleiten unsere Kunden mit Passion und Sachverstand durch jede Phase des Verkaufsprozesses.</p>
    <ul>
      <li>Erstes Gespräch und Besichtigung der Immobilie</li>
      <li>Ermitteln des bestmöglichen Verkaufspreises</li>
      <li>Erstellen von Verkaufsunterlagen und Vermarktung des Objekts</li>
      <li>Qualifizieren der Kaufinteressenten</li>
      <li>Finanzierungsberatung für Kaufinteressenten</li>
      <li>Preisverhandlung und Ausarbeiten des Kaufvertrags</li>
      <li>Begleitung bei der Beurkundung und Eigentumsübertragung</li>
    </ul>
  </div>
  <div class="abs side-label" style="top:272px">Schätzung des<br>Immobilienwerts</div>
  <div class="abs body-copy" style="top:270px">
    <p>Damit unsere Kunden den bestmöglichen Preis für ihr Haus, ihre Eigentumswohnung oder ihr Grundstück erzielen, ermitteln wir den genauen Wert. Unsere Schätzung ergibt eine übersichtliche Aufstellung zum Gebäude, der Lage, dem wirtschaftlichen Wert und Angaben zum Verkehrswert der Immobilie.</p>
    <p>Wir wenden je nach Objekt die folgenden Bewertungsmethoden an:</p>
    <ul>
      <li>Sachwert-, Ertragswert- oder Mischwertmethode</li>
      <li>Hedonische Bewertungen, Residualwertverfahren oder DCF (Discounted-Cash-Flow Verfahren)</li>
    </ul>
  </div>

  <div class="abs contact-band"></div>
  <div class="abs brand inside-brand"><span class="brand-square"></span>NORVALA</div>
  <div class="abs contact-box">
    <div class="contact-name">Norvala Immobilien AG</div>
    Lindenweg 12<br>8003 Zürich
    <div class="contact-cols">
      <span>T:&nbsp; +41 44 210 37 80<br>F:&nbsp; +41 44 210 37 85</span>
      <span>info@norvala-immo.ch<br>www.norvala-immo.ch</span>
    </div>
  </div>

  <div class="abs perforation"></div>
  <svg class="abs scissors" viewBox="0 0 18 22" aria-hidden="true" fill="none" stroke="#27a9d6" stroke-width="1.4">
    <circle cx="5" cy="17" r="3"/><circle cx="13" cy="17" r="3"/>
    <line x1="6.5" y1="14.5" x2="13" y2="1"/><line x1="11.5" y1="14.5" x2="5" y2="1"/>
  </svg>

  <div class="abs tape tape--top">KLEBESTREIFEN</div>
  <div class="abs values-frame"></div>
  <div class="abs values-frame-topleft"></div>
  <div class="abs values-frame-left"></div>
  <h2 class="abs headline values-title">Unsere Werte &amp; Visionen</h2>
  <p class="abs values-copy">Jede Immobilie ist so einzigartig, wie die Menschen, denen sie gehört. Für uns zählt der Mensch, die Liegenschaft und die gemeinsame Geschichte. In über 20 Jahren haben wir das Immobiliengeschäft und all seine Facetten verinnerlicht. Das macht uns zu einem kompetenten und engagierten Partner für alle Fragen rund um Immobilien.</p>
  <div class="abs quote-mark">”</div>
  <p class="abs quote-text">Immobilien sind unsere Passion<br>und die Zufriedenheit der Kunden<br>ist unser Ziel.</p>

  <div class="abs fold-note">Bitte 1x falten und an den Klebestreifen zusammenkleben</div>
  <div class="abs fold-line"></div>

  <h2 class="abs headline reply-title">Rückantwort <span class="slash">/</span></h2>
  <p class="abs reply-intro">Bitte kreuzen Sie Ihre Wünsche an:</p>
  <ul class="abs checklist">
    <li>... wir denken über einen Verkauf unserer Immobilie nach</li>
    <li>... wir sind am Kauf einer Wohnung / Haus interessiert</li>
    <li>... wir wünschen ein unverbindliches persönliches Gespräch</li>
  </ul>
  <div class="field" style="left:427px;top:420px">Name / Vorname</div>
  <div class="field" style="left:427px;top:452px">Strasse / Nr.</div>
  <div class="field" style="left:584px;top:452px">PLZ / Ort</div>
  <div class="field" style="left:427px;top:484px">Telefon</div>
  <div class="field" style="left:584px;top:484px">E-Mail</div>

  <div class="abs tape tape--bottom">KLEBESTREIFEN</div>
</section>
<div class="captions captions--inside"><span>Innen - Links</span><span>Innen - Rechts</span></div>

</body>
</html>
```